Tradie Thursday - A5 double sided pamphlet/brochure

We need a 1 page, double sided brochure made for a new themed night at our club…Tradie Thursday.

Our club is Velvetlane Lounge 47. However, this brochure is to have nothing sexual about it.

The theme is to be "Tradies"... Tradesman - painters, builders etc

We want it to be fairly simple. Very easy to read and to the point.

I have attached our logo - MUST BE ON THE BROCHURE

I have also attached a rough draft of the look. But it is very basic. We want something that looks much better than this! You DO NOT need to follow this layout.

This is to be a 1 Page, double sided, size: A5

It is to have the following information:

Title: Tradie Thursday
Kicks off June 2nd
Bar snacks
Front door prices
Quarterdeck Bar access 3-9pm
Entry to main showroom after 9pm (dress code applies)

Lucky Draw every hour
Win: VIP Memberships, Entertainment vouchers and more!

Small text:
83 Wattle Rd, Melbourne
9351 7206
www.lounge47.com.au

Very small text:
Sexually explicit material may offend
18+ only

Target Market(s)

young men, in the tradesman field of work, men who drink/go out/hang with their mates.

Industry/Entity Type

Club

Requirements
Must have
• Must have our logo
Nice to have
• The tradesman theme means it is masculine and for workers.

So anything with hazzard tape, road signs, machinery etc (but still general enough for all fields of work)

We are a (strip) club. So something conservative but maybe beer, or a bit of a nightclub look to the front page will be fine.

The main thing is to keep it simple and easy to read.
Should not have
• Nothing sexual.

There are still some women in trade work, and we don't want to offend.

```html
<!DOCTYPE html>
<html lang="en">
<head>
<meta charset="utf-8">
<title>Tradie Thursday – Velvetlane Lounge 47</title>
<link href="https://fonts.googleapis.com/css2?family=Archivo+Black&family=Roboto+Condensed:wght@400;700&display=swap" rel="stylesheet">
<style>
  :root {
    --backdrop: #d8d5d1;
    --ink: #050505;
    --frame: #8d8d8d;
    --red: #d42a2a;
    --red-dark: #8e1515;
    --wine: #7a0d12;
    --yellow: #ffee1f;
    --white: #ffffff;
    --muted: #9a9a9a;
    --steel: #a9a9a9;
    --steel-dark: #5e5e5e;
    --body-font: "Roboto Condensed", Arial, sans-serif;
    --title-font: "Archivo Black", Arial, sans-serif;
  }
  * { margin: 0; padding: 0; box-sizing: border-box; }
  html, body { width: 1200px; height: 824px; overflow: hidden; }
  body { background: var(--backdrop); position: relative; font-family: var(--body-font); }

  .flyer { position: absolute; background: var(--ink); overflow: hidden; }
  .flyer--front { left: 42px; top: 32px; width: 543px; height: 759px; }
  .flyer--cover { left: 611px; top: 32px; width: 547px; height: 761px; border: 7px solid var(--frame); }

  .decor { position: absolute; }
  .front-decor {
    left: 40px; top: 10px; width: 463px; height: 190px;
    background: radial-gradient(closest-side, #b52020 0%, #4a4a4a 45%, #1b1b1b 75%, transparent 100%);
  }
  .cover-decor {
    left: 40px; top: 95px; width: 453px; height: 320px;
    background: radial-gradient(closest-side, #a91d1d 0%, #3f3f3f 50%, #151515 80%, transparent 100%);
  }

  .kickoff { position: absolute; width: 100%; text-align: center; font-weight: 700; font-size: 22px; }
  .flyer--front .kickoff { top: 158px; color: var(--yellow); }
  .flyer--cover .kickoff { top: 512px; color: var(--white); }

  .title-block { position: absolute; left: 0; top: 192px; width: 100%; text-align: center; }
  .title-block span {
    display: block; font-family: var(--title-font); font-size: 50px; line-height: 46px; letter-spacing: 1px;
    color: var(--steel); text-shadow: 0 2px 0 #dcdcdc, 0 5px 0 var(--steel-dark);
  }

  .info-panel {
    position: absolute; left: 19px; top: 296px; width: 504px; height: 150px;
    background: linear-gradient(#9d9d9d, #6f6f6f); border: 2px solid #c8c8c8;
  }
  .beer-art {
    position: absolute; left: 9px; top: 22px; width: 78px; height: 100px;
    background: linear-gradient(#fff7d8 0%, #f2b021 30%, #d88a0e 100%); border-radius: 6px;
  }
  .lucky-draw { position: absolute; left: 96px; top: 20px; width: 128px; text-align: center; }
  .lucky-draw strong { display: block; color: var(--red); font-size: 40px; line-height: 38px; font-weight: 700; }
  .lucky-draw small { display: block; color: var(--white); font-size: 13px; margin-top: 6px; }
  .perks { position: absolute; left: 270px; top: 16px; list-style: none; }
  .perks li { color: var(--yellow); font-weight: 700; font-size: 23px; line-height: 29px; }

  .ribbon { position: absolute; left: 0; top: 446px; width: 543px; height: 104px; }
  .ribbon-text {
    position: absolute; left: 0; top: 460px; width: 100%; text-align: center;
    color: var(--white); font-weight: 700; font-size: 22px; line-height: 30px;
  }

  .win { position: absolute; top: 590px; width: 100%; text-align: center; color: var(--white); }
  .win h2 { font-family: var(--body-font); font-weight: 700; font-size: 46px; line-height: 52px; }
  .win p { font-size: 19px; line-height: 25px; }

  .contact-bar {
    position: absolute; left: 9px; top: 706px; width: 523px; height: 32px;
    background: var(--red-dark); color: var(--white); font-size: 15px;
    display: flex; align-items: center; justify-content: center; gap: 10px;
  }
  .small-print {
    position: absolute; left: 0; top: 742px; width: 100%; text-align: center;
    color: var(--muted); font-size: 10px; line-height: 12px;
  }

  .brand {
    position: absolute; left: 0; top: 212px; width: 100%; text-align: center;
    color: var(--white); font-family: var(--body-font); font-weight: 700; font-size: 46px; line-height: 48px;
  }
  .arched-title { position: absolute; left: 0; top: 378px; width: 533px; height: 170px; }
  .arched-title text { font-family: var(--title-font); fill: var(--steel); }
  .arched-title .arch-top { font-size: 54px; }
  .arched-title .arch-bottom { font-size: 58px; }
  .glasses-art {
    position: absolute; left: 60px; top: 555px; width: 413px; height: 195px;
    background:
      radial-gradient(closest-side, var(--wine) 0%, #3b0508 55%, transparent 100%) 0 0 / 50% 100% no-repeat,
      radial-gradient(closest-side, var(--wine) 0%, #3b0508 55%, transparent 100%) 100% 0 / 50% 100% no-repeat;
  }
</style>
</head>
<body>

<section class="flyer flyer--front">
  <div class="decor front-decor" role="img" aria-label="Red star framed by silver swirl ornaments"></div>
  <p class="kickoff">Kicks off June 2nd</p>
  <h1 class="title-block"><span>TRADIE</span><span>THURSDAY</span></h1>

  <div class="info-panel">
    <div class="beer-art" role="img" aria-label="Pint of beer"></div>
    <div class="lucky-draw"><strong>LUCKY<br>DRAW</strong><small>*EVERY HOUR*</small></div>
    <ul class="perks">
      <li>Bar snacks</li>
      <li>Front door prices</li>
      <li>Quarterdeck Bar</li>
      <li>Access 3-9pm</li>
    </ul>
  </div>

  <svg class="ribbon" viewBox="0 0 543 104" aria-hidden="true">
    <polygon points="0,104 40,30 88,30 88,104" fill="var(--red-dark)"/>
    <polygon points="543,104 503,30 455,30 455,104" fill="var(--red-dark)"/>
    <polygon points="62,8 481,8 500,88 43,88" fill="var(--red)"/>
  </svg>
  <p class="ribbon-text">Entry to main showroom after<br>9pm (dress code applies)</p>

  <div class="win">
    <h2>WIN...</h2>
    <p>VIP Memberships, Entertainment<br>vouchers and more!</p>
  </div>

  <footer class="contact-bar">
    <span>83 Wattle Rd, Melbourne</span><span>|</span><span>9351 7206</span><span>|</span><span>www.lounge47.com.au</span>
  </footer>
  <p class="small-print">Sexually explicit material may offend &nbsp;|&nbsp; 18+ only</p>
</section>

<section class="flyer flyer--cover">
  <div class="decor cover-decor" role="img" aria-label="Red star framed by silver swirl ornaments"></div>
  <p class="brand">Velvetlane<br>Lounge 47</p>
  <svg class="arched-title" viewBox="0 0 533 170" aria-label="Tradie Thursday">
    <defs>
      <path id="arch-top" d="M70,88 Q243,18 417,88"/>
      <path id="arch-bottom" d="M40,160 Q263,50 486,160"/>
    </defs>
    <text class="arch-top" text-anchor="middle"><textPath href="#arch-top" startOffset="50%" textLength="330" lengthAdjust="spacing">TRADIE</textPath></text>
    <text class="arch-bottom" text-anchor="middle"><textPath href="#arch-bottom" startOffset="50%" textLength="450" lengthAdjust="spacing">THURSDAY</textPath></text>
  </svg>
  <p class="kickoff">Kicks off June 2nd</p>
  <div class="glasses-art" role="img" aria-label="Two glasses of red wine clinking with a splash"></div>
</section>

</body>
</html>
```